Harborline Motors LLC

Car Dealer Customer Service
Address: 2741 Linden Avenue, Shelbyville, TN 37162
web: www.harborlinemotorstn.net
email: harborlinemotorstn@mailbox-example.net
Phone: (931) 555-0148
Phone: (629) 555-0173

```html
<!DOCTYPE html>
<html lang="en">
<head>
<meta charset="utf-8">
<title>Harborline Motors LLC – Business Card</title>
<link rel="stylesheet" href="https://fonts.googleapis.com/css2?family=Poppins:wght@400;600;700&family=Roboto+Condensed:wght@700&display=swap">
<style>
  :root {
    --bg: #2b2b2d;
    --card: #232326;
    --card-dark: #1c1c1f;
    --gold: #e4a93a;
    --blue: #1f7fbf;
    --blue-light: #2a90d2;
    --white: #f2f2f2;
    --emboss: #18181a;
  }
  * { margin: 0; padding: 0; box-sizing: border-box; }
  html, body { width: 1200px; height: 1138px; overflow: hidden; background: var(--bg); }
  body { position: relative; font-family: "Poppins", sans-serif; color: var(--white); }

  .card {
    position: absolute;
    left: 290px;
    width: 620px;
    height: 372px;
    border-radius: 16px;
    overflow: hidden;
    background: linear-gradient(160deg, var(--card) 0%, var(--card-dark) 100%);
  }
  .card--front { top: 186px; }
  .card--back { top: 608px; }

  /* Front */
  .front-name {
    position: absolute;
    left: 0; right: 0; top: 150px;
    text-align: center;
    font-weight: 700;
    font-size: 34px;
    letter-spacing: 1px;
    color: var(--emboss);
    text-transform: uppercase;
  }
  .front-web {
    position: absolute;
    left: 0; right: 0; top: 333px;
    display: flex; align-items: center; justify-content: center; gap: 22px;
    font-size: 14px;
    color: var(--white);
  }
  .front-web .rule { width: 52px; height: 2px; background: var(--gold); }

  /* Back */
  .phones {
    position: absolute; left: 28px; top: 56px;
    font-family: "Roboto Condensed", sans-serif;
    font-weight: 700; font-size: 27px; line-height: 30px;
  }
  .phone-row { display: flex; align-items: center; gap: 10px; }
  .phone-row svg { width: 20px; height: 18px; fill: var(--gold); }

  .brand {
    position: absolute; left: 330px; top: 206px; width: 260px;
    display: flex; align-items: center; justify-content: center; gap: 10px;
    font-weight: 700; font-size: 22px; color: var(--blue-light);
    text-transform: uppercase; white-space: nowrap;
  }
  .brand .dot { width: 12px; height: 12px; border-radius: 50%; background: var(--gold); }

  .wave { position: absolute; left: 0; top: 0; width: 620px; height: 372px; }

  .contact {
    position: absolute; left: 30px; top: 256px;
    font-size: 14.5px; line-height: 20px; color: var(--white);
  }
  .contact .address { margin-bottom: 8px; }
  .contact-row { display: flex; align-items: center; gap: 9px; }
  .contact-row svg { width: 12px; height: 12px; }
</style>
</head>
<body>

<section class="card card--front">
  <div class="front-name">Harborline Motors</div>
  <div class="front-web">
    <span class="rule"></span>
    <span>www.harborlinemotorstn.net</span>
    <span class="rule"></span>
  </div>
</section>

<section class="card card--back">
  <svg class="wave" viewBox="0 0 620 372" aria-hidden="true">
    <path d="M0,206 C60,190 130,182 230,222 C330,262 420,318 520,300 C570,292 600,282 620,276 L620,372 L0,372 Z" fill="var(--gold)"/>
    <path d="M0,214 C70,198 140,192 240,232 C340,272 430,326 530,310 C575,302 605,292 620,288 L620,372 L0,372 Z" fill="var(--card-dark)"/>
    <defs>
      <linearGradient id="blueFill" x1="0" y1="0" x2="1" y2="1">
        <stop offset="0" stop-color="#1a6fa8"/>
        <stop offset="1" stop-color="#2185c6"/>
      </linearGradient>
    </defs>
    <path d="M0,226 C70,212 150,212 250,252 C350,292 440,342 540,324 C580,318 605,310 620,306 L620,372 L0,372 Z" fill="url(#blueFill)"/>
    <path d="M320,294 C400,318 480,322 590,288 C500,312 420,314 320,294 Z" fill="var(--gold)"/>
  </svg>

  <div class="phones">
    <div class="phone-row">
      <svg viewBox="0 0 20 18"><path d="M2 5 C2 2 6 1 10 1 C14 1 18 2 18 5 L18 7 L14 7 L14 5 L6 5 L6 7 L2 7 Z M5 8 L15 8 L18 17 L2 17 Z"/></svg>
      <span>931-555-0148</span>
    </div>
    <div class="phone-row">
      <svg viewBox="0 0 20 18"><path d="M2 5 C2 2 6 1 10 1 C14 1 18 2 18 5 L18 7 L14 7 L14 5 L6 5 L6 7 L2 7 Z M5 8 L15 8 L18 17 L2 17 Z"/></svg>
      <span>629-555-0173</span>
    </div>
  </div>

  <div class="brand"><span class="dot"></span><span>Harborline Motors</span></div>

  <div class="contact">
    <p class="address">2741 Linden Avenue,<br>Shelbyville, TN 37162</p>
    <p class="contact-row">
      <svg viewBox="0 0 12 12"><rect x="0.5" y="2" width="11" height="8" fill="var(--gold)"/><path d="M0.5 2 L6 7 L11.5 2" stroke="#1a6fa8" fill="none"/></svg>
      <span>www.harborlinemotorstn.net</span>
    </p>
    <p class="contact-row">
      <svg viewBox="0 0 12 12"><circle cx="6" cy="6" r="5.5" fill="var(--gold)"/><path d="M0.5 6 H11.5 M6 0.5 V11.5" stroke="#1a6fa8" stroke-width="0.8"/></svg>
      <span>harborlinemotorstn@mailbox-example.net</span>
    </p>
  </div>
</section>

</body>
</html>
```